Business Card Design Project

Hello
I want a Simple Business card that uses the company logo that is easily reasonable but looks professional as I am an IT Services company and would look to share these cards with prospective clients.
The details are:
Kelvo Ridge Solutions
14 Marlow Crescent
Birmingham
B7 4QT
Telephone 0845 271 6049
I would like my name Gareth Wilcombe and my title Director on the card.
Target Market(s)
IT Professionals
Industry/Entity Type
Business

```html
<!DOCTYPE html>
<html lang="en">
<head>
<meta charset="utf-8">
<title>Kelvo Ridge Solutions – Business Card</title>
<link href="https://fonts.googleapis.com/css2?family=Didact+Gothic&display=swap" rel="stylesheet">
<style>
  :root {
    --ink: #231f20;
    --text: #1c1c1c;
    --bg-light: #ffffff;
    --bg-mid: #ececec;
    --bg-dark: #cfcfcf;
    --leaf-green: #7cc352;
    --accent-yellow: #eeea6c;
    --mark-green: #8fcb5f;
  }
  html, body {
    margin: 0;
    padding: 0;
    overflow: hidden;
    width: 1200px;
    height: 667px;
  }
  .card {
    position: relative;
    width: 1200px;
    height: 667px;
    overflow: hidden;
    background: radial-gradient(ellipse 900px 700px at 640px 40px, var(--bg-light) 0%, var(--bg-mid) 55%, var(--bg-dark) 100%);
    font-family: "Didact Gothic", sans-serif;
    color: var(--text);
  }
  .corner-sweep {
    position: absolute;
    inset: 0;
  }
  .brand {
    position: absolute;
    left: 0;
    width: 1200px;
    top: 40px;
    text-align: center;
    color: var(--ink);
  }
  .brand-dot {
    display: block;
    width: 120px;
    height: 120px;
    margin: 0 auto 4px;
    border-radius: 50%;
    background: var(--mark-green);
  }
  .brand-name {
    display: block;
    font-size: 96px;
    line-height: 1;
    letter-spacing: 1px;
  }
  .brand-tag {
    display: block;
    font-size: 28px;
    letter-spacing: 5px;
    margin-top: 4px;
    padding-left: 240px;
  }
  .contact-title {
    position: absolute;
    left: 41px;
    top: 315px;
    margin: 0;
    font-size: 42px;
    font-weight: 400;
    letter-spacing: 0.5px;
  }
  .contact-row {
    position: absolute;
    display: flex;
    align-items: center;
    font-size: 40px;
    letter-spacing: 1px;
  }
  .contact-row svg { fill: var(--ink); flex: none; }
  .contact-phone { left: 47px; top: 397px; }
  .contact-phone svg { margin-right: 30px; }
  .contact-address { left: 40px; top: 514px; }
  .contact-address svg { margin-right: 12px; }
</style>
</head>
<body>
<main class="card">
  <svg class="corner-sweep" width="1200" height="667" viewBox="0 0 1200 667" aria-hidden="true">
    <path d="M700 667 Q1010 560 1200 225 L1200 667 Z" fill="var(--accent-yellow)"/>
    <path d="M724 667 Q1020 566 1200 250 L1200 667 Z" fill="var(--leaf-green)"/>
  </svg>

  <div class="brand">
    <span class="brand-dot"></span>
    <span class="brand-name">kelvo ridge</span>
    <span class="brand-tag">solutions</span>
  </div>

  <h1 class="contact-title">Director: Gareth Wilcombe</h1>

  <div class="contact-row contact-phone">
    <svg width="54" height="76" viewBox="0 0 54 76" aria-label="Telephone" role="img">
      <rect x="38" y="0" width="5" height="10" rx="2"/>
      <rect x="0" y="8" width="54" height="68" rx="8"/>
      <rect x="8" y="16" width="38" height="22" rx="2" fill="#e4e4e4"/>
      <g fill="#e4e4e4">
        <circle cx="14" cy="48" r="3.5"/><circle cx="27" cy="48" r="3.5"/><circle cx="40" cy="48" r="3.5"/>
        <circle cx="14" cy="58" r="3.5"/><circle cx="27" cy="58" r="3.5"/><circle cx="40" cy="58" r="3.5"/>
        <circle cx="14" cy="68" r="3.5"/><circle cx="27" cy="68" r="3.5"/><circle cx="40" cy="68" r="3.5"/>
      </g>
    </svg>
    <span>: 0845 271 6049</span>
  </div>

  <div class="contact-row contact-address">
    <svg width="72" height="68" viewBox="0 0 72 68" aria-label="Address" role="img">
      <path d="M36 0 L72 32 L64 32 L64 68 L44 68 L44 46 L28 46 L28 68 L8 68 L8 32 L0 32 Z"/>
      <rect x="50" y="4" width="9" height="18"/>
    </svg>
    <span>: 14 Marlow Crescent; Birmingham; B7 4QT</span>
  </div>
</main>
</body>
</html>
```